dentist office tri-fold for root canal specialist

design a tri fold brochure to give to patients talking about the office and the services
Talk about doctors and their bios
services: root canal , retreatments, endodontic surgery, trauma, cracked teeth
Technology: CBCT, microscopes, lasers, clear pulse advanced
I will provide all the technical info. willing to hire a writer if needed. Attached a picture of our logo as a reference of our colors. Can attach older versions of brochure if requested. Looking for a very professional tri fold that will be used to market the practice to patients and other doctors.
Rough idea: TRIFOLD
Front Cover:
Welcome to The Halvern Team
Thank you for allowing us to care for your endodontic needs. We look forward to serving you.
We at The Halvern Team have dedicated our professional lives to improving the comfort and dental health of those in our care.
Inner Right:
Pics of Docs
Welcome – On behalf of our staff, we welcome you to our office.
We are pleased that you have selected our team of professionals to care for your endodontic needs. We want you to know that we are committed to providing you, our patient with the highest quality endodontic care in the most gentle, efficient, and caring manner possible. We pride ourselves on offering our expertise along with the best patient care with the most up to date technologies to better ensure your oral health.
For your convenience, please visit us online at www.thehalvernteam.com for directions to our offices, pre and post-operative instructions, general information on our Endodontists and much more. We are here for you and our doctors are on call 24 hours a day, 7 days a week.
We are looking forward providing you a most relaxed and pleasant vist possible. Thank you again for choosing The Halvern Team.
Inner Middle:
What is a Root Canal?
A root canal (endodontic treatment) is one of the most common dental procedures performed, with more than 14 million performed every year. This simple treatment can save your natural teeth and prevent the need of dental implants or bridges.
At the center of your tooth is pulp. The pulp is a collection of blood vessels, nerves and lymphatics, which help to form the tooth during the stages of tooth development.
I’ve already had a root canal, why do I need another procedure?
Retreatment - A second chance to save your tooth
With proper care, most teeth which have had endodontic (root canal) treatment can last as long as other natural teeth.
However, in a few cases, a tooth that has received endodontic treatment fails to heal completely. And occasionally, a tooth becomes painful or diseased months or even years after previously successful endodontic treatment.
If your tooth has failed to heal or has developed new problems, you have a second chance. Another endodontic procedure, called retreatment, may be able to save your tooth.
Retreated teeth can function well for years, even for a lifetime. It's always best to save the tooth if your endodontist believes retreatment is the best option for you.
Advances in technology are constantly changing the way root canal treatment is performed, so your endodontist may even be able to use a new technique that was not available when you had your first procedure.
Of course, there are no guarantees with any dental or medical procedure. Your endodontist will discuss your options and the chances of success before beginning retreatment.
What is an Apicoectomy?
In this procedure, the endodontist opens the gum tissue near the tooth to see the underlying bone and to remove any inflamed or infected tissue. The very end of the root is also removed or resected.
Inner Right:
Patient Care: Needing a root canal is often a surprise and sometimes an emergency. We at The Halvern Team make certain that every patient receives prompt emergency care at any time.
We understand how uneasy some patients may feel about dental visits and how we can make a difference in providing a relaxing, positive experience. Our doctors are trained in different levels of sedation dentistry from Nitrous Oxide to Conscious Sedation.
Our entire team is dedicated to providing you with excellent, personalized care and service to make your visit as comfortable and pleasant as possible. You will enjoy our relaxing treatment rooms, complete with plumacore coverings, televisions and Tunelets for your use during treatment and blankets to keep you warm if you’re cold.
Technical Equipment: The Halvern Team prides itself in utilizing the most advanced techniques and state-of-the-art equipment including digital radiography, fiber optic illumination, ultrasonic equipment, and operating microscopes, which help the doctor see microscopic details inside a tooth during micro-surgical and non-surgical procedures.
Expertise: The Halvern Team is staffed by doctors who are responsive to your concerns and alert to your experience during treatment. All of our doctors are endodontists, which means they are specialists who have completed 2-3 years of advanced training in addition to dental school. We are all specialist members of the Continental Society of Pulp Specialists (CSPS). All our endodontists continue their education and training through professional associations, seminars, study groups, and teaching both at Pellmoor and Dorrin Universities.

```html
<!DOCTYPE html>
<html lang="en">
<head>
<meta charset="utf-8">
<title>The Halvern Team – Tri-fold Brochure</title>
<link href="https://fonts.googleapis.com/css2?family=Poppins:wght@400;500;600;700&display=swap" rel="stylesheet">
<style>
:root{
  --navy:#1b2c6b;
  --navy-deep:#13215a;
  --navy-mid:#2d3f86;
  --ink:#222;
  --white:#fff;
  --page:#e9ebf0;
  --photo-a:#c9d3e2;
  --photo-b:#8ea3c3;
}
*{margin:0;padding:0;box-sizing:border-box}
html,body{width:823px;height:1200px;overflow:hidden}
body{background:var(--page);font-family:"Poppins",sans-serif;color:var(--ink);position:relative}
.sheet{position:absolute;left:94px;width:634px;height:489px;background:var(--white);overflow:hidden;box-shadow:0 2px 8px rgba(0,0,0,.15)}
.sheet--outside{top:67px}
.sheet--inside{top:632px}
.shapes{position:absolute;inset:0}
.abs{position:absolute}
.body-text{font-size:5.6px;line-height:9.4px}
.body-text p+p{margin-top:9px}
.body-text--white{color:var(--white)}
strong{font-weight:600}

/* outside sheet */
.welcome-title{left:18px;top:130px;width:180px;font-size:9.5px;line-height:12px}
.welcome-title b{font-size:12px;font-weight:600}
.welcome-body{left:18px;top:173px;width:172px}
.office{left:18px;width:190px;font-size:6.8px;line-height:13px}
.office h4{font-size:6.8px;font-weight:600;color:var(--navy);padding-left:22px}
.office p{padding-left:22px}
.office svg{position:absolute;left:1px;top:3px}
.office--a{top:380px}
.office--b{top:434px}
.smile-title{left:230px;top:18px;width:180px;color:var(--white);font-size:16.5px;font-weight:600;line-height:25px}
.brand-name{left:232px;top:253px;width:170px;font-size:10px;color:var(--navy);font-weight:500;letter-spacing:.3px}
.thanks{left:232px;top:290px;width:170px;text-align:center;color:var(--navy);font-size:7.6px;line-height:12px}
.site{font-size:7.6px;color:var(--navy)}
.site--front{left:233px;top:454px}
.spine-name{left:596px;top:245px;transform-origin:0 0;transform:rotate(-90deg);font-size:17px;color:var(--navy);letter-spacing:1px;white-space:nowrap;font-weight:400}
.cover-welcome{left:442px;top:372px;width:160px;color:var(--white)}
.cover-welcome h2{font-size:10.5px;font-weight:600;line-height:14px}
.cover-welcome h3{font-size:10.5px;font-weight:400;line-height:14px}
.cover-welcome p{font-size:7.6px;line-height:12px;margin-top:10px}

/* inside sheet */
.rc-title{left:11px;top:234px;font-size:17px;font-weight:600;color:var(--navy);line-height:25px}
.rc-body{left:11px;top:298px;width:190px}
.site--back{left:38px;top:469px;color:var(--white)}
.retreat{left:225px;top:14px;width:190px}
.retreat h2{font-size:11.5px;font-weight:600;color:var(--white);line-height:15px}
.retreat h5{font-size:6px;font-style:italic;font-weight:600;color:var(--white);margin:10px 0 4px}
.retreat .body-text p+p{margin-top:6px}
.apico{left:225px;top:375px;width:190px}
.apico h2{font-size:11.5px;font-weight:600;color:var(--navy);line-height:17px}
.apico .body-text{margin-top:9px}
.care{left:435px;top:14px;width:187px}
.care h2{font-size:11.5px;font-weight:600;color:var(--white)}
.care .body-text{margin-top:10px}
.care .body-text p+p{margin-top:7px}
.tech{left:435px;top:262px;width:187px}
.tech h2{font-size:11.5px;font-weight:600;color:var(--ink);line-height:15px}
.tech .body-text{margin-top:10px}
.tech .body-text p+p{margin-top:7px}
</style>
</head>
<body>

<!-- Outside sheet -->
<section class="sheet sheet--outside">
  <svg class="shapes" width="634" height="489" viewBox="0 0 634 489">
    <defs>
      <linearGradient id="navyGrad" x1="0" y1="0" x2="1" y2="1">
        <stop offset="0" stop-color="#2a3d86"/><stop offset="1" stop-color="#13215a"/>
      </linearGradient>
    </defs>
    <path d="M211 0 H430 C440 40 420 70 400 95 C380 118 380 150 395 185 H211 Z" fill="url(#navyGrad)"/>
    <path d="M395 185 C370 150 372 120 392 97" fill="none" stroke="#c9cfe0" stroke-width="0"/>
    <path d="M354 489 C354 410 370 360 430 350 C500 340 560 355 600 340 C615 334 626 325 634 318 V489 Z" fill="url(#navyGrad)"/>
  </svg>
  <svg class="abs" style="left:0;top:0" width="211" height="120" viewBox="0 0 211 120" role="img" aria-label="Photo of the endodontist team in white coats">
    <defs><linearGradient id="teamGrad" x1="0" y1="0" x2="0" y2="1"><stop offset="0" stop-color="#dfe4ec"/><stop offset="1" stop-color="#b9c3d3"/></linearGradient></defs>
    <path d="M0 0 H211 V110 C170 80 130 95 90 100 C50 105 20 100 0 110 Z" fill="url(#teamGrad)"/>
    <path d="M0 112 C30 100 60 104 95 100 C140 94 175 84 211 115" fill="none" stroke="var(--navy)" stroke-width="3"/>
  </svg>
  <div class="abs welcome-title"><b>Welcome</b> – On behalf of our staff, we welcome you to our office.</div>
  <div class="abs body-text welcome-body">
    <p>We are pleased that you have selected our team of professionals to care for your endodontic needs. We want you to know that we are committed to providing you, our patient with the highest quality endodontic care in the most gentle, efficient, and caring manner possible. We pride ourselves on offering our expertise along with the best patient care with the most up to date technologies to better ensure your oral health.</p>
    <p>For your convenience, please visit us online at <strong>www.thehalvernteam.com</strong> for directions to our offices, pre and post-operative instructions, general information on our Endodontists and much more. We are here for you and our doctors are on call 24 hours a day, 7 days a week.</p>
    <p>We are looking forward providing you a most relaxed and pleasant vist possible. Thank you again for choosing The Halvern Team.</p>
  </div>
  <div class="abs office office--a">
    <svg width="13" height="17" viewBox="0 0 13 17"><path d="M6.5 0C2.9 0 0 2.9 0 6.4 0 11 6.5 17 6.5 17S13 11 13 6.4C13 2.9 10.1 0 6.5 0Z" fill="var(--navy)"/><circle cx="6.5" cy="6.4" r="2.6" fill="#fff"/></svg>
    <h4>ASHBURY OFFICE</h4>
    <p>212 Linden Avenue, Ashbury, MA 01080</p>
    <p>Tel: 555-014-2290</p>
  </div>
  <div class="abs office office--b">
    <svg width="13" height="17" viewBox="0 0 13 17"><path d="M6.5 0C2.9 0 0 2.9 0 6.4 0 11 6.5 17 6.5 17S13 11 13 6.4C13 2.9 10.1 0 6.5 0Z" fill="var(--navy)"/><circle cx="6.5" cy="6.4" r="2.6" fill="#fff"/></svg>
    <h4>CORWELL OFFICE</h4>
    <p>48 Harbor Lane, Corwell, MA 01091</p>
    <p>Tel: 555-016-7731</p>
  </div>

  <h1 class="abs smile-title">We can't wait to see you smile</h1>
  <svg class="abs" style="left:244px;top:76px" width="150" height="150" viewBox="0 0 150 150" role="img" aria-label="Close-up photo of a bright smile">
    <defs><radialGradient id="smileGrad"><stop offset="0" stop-color="#f2dcd3"/><stop offset="1" stop-color="#dba99c"/></radialGradient></defs>
    <circle cx="75" cy="75" r="71" fill="url(#smileGrad)" stroke="var(--navy)" stroke-width="4"/>
  </svg>
  <div class="abs brand-name">The Halvern Team</div>
  <p class="abs thanks">Thank you for allowing us to care for your endodontic needs. We look forward to serving you.</p>
  <div class="abs site site--front">www.thehalvernteam.com</div>

  <div class="abs spine-name">The Halvern Team</div>
  <div class="abs cover-welcome">
    <h2>Welcome to</h2>
    <h3>The Halvern Team</h3>
    <p>We at The Halvern Team have dedicated our professional lives to improving the comfort and dental health of those in our care.</p>
  </div>
</section>

<!-- Inside sheet -->
<section class="sheet sheet--inside">
  <svg class="shapes" width="634" height="489" viewBox="0 0 634 489">
    <defs>
      <linearGradient id="navyGrad2" x1="0" y1="0" x2="1" y2="1">
        <stop offset="0" stop-color="#2a3d86"/><stop offset="1" stop-color="#13215a"/>
      </linearGradient>
    </defs>
    <path d="M212 0 H422 V300 C405 330 385 352 360 350 C320 345 260 340 212 300 Z" fill="url(#navyGrad2)"/>
    <path d="M422 0 H634 V235 C600 240 590 225 560 235 C520 245 470 235 430 260 L422 265 Z" fill="url(#navyGrad2)"/>
    <path d="M0 430 C20 400 60 385 120 395 C180 405 205 440 215 489 H0 Z" fill="url(#navyGrad2)"/>
  </svg>
  <svg class="abs" style="left:0;top:0" width="212" height="240" viewBox="0 0 212 240" role="img" aria-label="Photo of model teeth in a dental lab">
    <defs><linearGradient id="teethGrad" x1="0" y1="0" x2="1" y2="1"><stop offset="0" stop-color="#eef1f6"/><stop offset="1" stop-color="#9fb0cc"/></linearGradient></defs>
    <path d="M0 0 H212 V235 C170 200 120 190 70 200 C40 206 15 215 0 225 Z" fill="url(#teethGrad)"/>
    <path d="M0 228 C30 208 80 196 130 200 C165 204 190 215 212 238" fill="none" stroke="var(--navy)" stroke-width="3"/>
  </svg>
  <h1 class="abs rc-title">What is a<br>Root Canal?</h1>
  <div class="abs body-text rc-body">
    <p>A root canal (endodontic treatment) is one of the most common dental procedures performed, with more than 14 million performed every year. This simple treatment can save your natural teeth and prevent the need of dental implants or bridges.</p>
    <p>At the center of your tooth is pulp. The pulp is a collection of blood vessels, nerves and lymphatics, which help to form the tooth during the stages of tooth development.</p>
  </div>
  <div class="abs site site--back">www.thehalvernteam.com</div>

  <div class="abs retreat">
    <h2>I’ve already had a root canal, why do I need another procedure?</h2>
    <h5>Retreatment – A second chance to save your tooth</h5>
    <div class="body-text body-text--white">
      <p>With proper care, most teeth which have had endodontic (root canal) treatment can last as long as other natural teeth. However, in a few cases, a tooth that has received endodontic treatment fails to heal completely. And occasionally, a tooth becomes painful or diseased months or even years after previously successful endodontic treatment. If your tooth has failed to heal or has developed new problems, you have a second chance. Another endodontic procedure, called retreatment, may be able to save your tooth.</p>
      <p>Retreated teeth can function well for years, even for a lifetime. It's always best to save the tooth if your endodontist believes retreatment is the best option for you. Advances in technology are constantly changing the way root canal treatment is performed, so your endodontist may even be able to use a new technique that was not available when you had your first procedure.</p>
      <p>Of course, there are no guarantees with any dental or medical procedure. Your endodontist will discuss your options and the chances of success before beginning retreatment.</p>
    </div>
  </div>
  <svg class="abs" style="left:310px;top:296px" width="108" height="108" viewBox="0 0 108 108" role="img" aria-label="Photo of a patient receiving a dental examination">
    <defs><linearGradient id="patientGrad" x1="0" y1="0" x2="1" y2="1"><stop offset="0" stop-color="#c9dcea"/><stop offset="1" stop-color="#7f9fc4"/></linearGradient></defs>
    <circle cx="54" cy="54" r="51" fill="url(#patientGrad)" stroke="var(--navy)" stroke-width="4"/>
  </svg>
  <div class="abs apico">
    <h2>What is an<br>Apicoectomy?</h2>
    <div class="body-text"><p>In this procedure, the endodontist opens the gum tissue near the tooth to see the underlying bone and to remove any inflamed or infected tissue. The very end of the root is also removed or resected.</p></div>
  </div>

  <div class="abs care">
    <h2>Patient Care:</h2>
    <div class="body-text body-text--white">
      <p>Needing a root canal is often a surprise and sometimes an emergency. We at The Halvern Team make certain that every patient receives prompt emergency care at any time.</p>
      <p>We understand how uneasy some patients may feel about dental visits and how we can make a difference in providing a relaxing, positive experience. Our doctors are trained in different levels of sedation dentistry from Nitrous Oxide to Conscious Sedation.</p>
      <p>Our entire team is dedicated to providing you with excellent, personalized care and service to make your visit as comfortable and pleasant as possible. You will enjoy our relaxing treatment rooms, complete with plumacore coverings, televisions and Tunelets for your use during treatment and blankets to keep you warm if you’re cold.</p>
    </div>
  </div>
  <svg class="abs" style="left:532px;top:202px" width="94" height="94" viewBox="0 0 94 94" role="img" aria-label="Photo of dental instruments on a tray">
    <defs><linearGradient id="toolsGrad" x1="0" y1="0" x2="1" y2="1"><stop offset="0" stop-color="#e4ecf4"/><stop offset="1" stop-color="#8aa6c8"/></linearGradient></defs>
    <circle cx="47" cy="47" r="44" fill="url(#toolsGrad)" stroke="var(--navy)" stroke-width="4"/>
  </svg>
  <div class="abs tech">
    <h2>Technical<br>Equipment</h2>
    <div class="body-text">
      <p>The Halvern Team prides itself in utilizing the most advanced techniques and state-of-the-art equipment including digital radiography, fiber optic illumination, ultrasonic equipment, and operating microscopes, which help the doctor see microscopic details inside a tooth during micro-surgical and non-surgical procedures.</p>
      <p>Expertise: The Halvern Team is staffed by doctors who are responsive to your concerns and alert to your experience during treatment. All of our doctors are endodontists, which means they are specialists who have completed 2-3 years of advanced training in addition to dental school. We are all specialist members of the Continental Society of Pulp Specialists (CSPS). All our endodontists continue their education and training through professional associations, seminars, study groups, and teaching both at Pellmoor and Dorrin Universities.</p>
    </div>
  </div>
</section>

</body>
</html>
```